Corvallin Property Solutions need a business card design

Hello guys. We would need a business card design asap please.
We are a start up property investment business based in London UK specialised in buying, selling, managing and letting properties and helping distressed property owners.
The name of our Business is Corvallin, the logo symbolises the four fundamental elements of the world (earth, air, fire and water) and so it stands for strength, stability, longevity.
We would like the business card to communicate professionalism and reliability. Many many thanks indeed for your work.

Details:

1.) Marisol Dunkley
Property Investor
Mobile: +44(0)7700362517
Email: marisol.corvallin@quilbrook.example

2.) Tomas Brindle
Property Investor
Mobile: +44(0)7700845926
Email: tomas.corvallin@quilbrook.example

Industry/Entity Type

Investment

```html
<!DOCTYPE html>
<html lang="en">
<head>
<meta charset="utf-8">
<title>Corvallin Property Solutions – Business Card</title>
<link rel="stylesheet" href="https://fonts.googleapis.com/css2?family=Josefin+Sans:wght@600;700&family=Questrial&display=swap">
<style>
  :root {
    --backdrop: #d6d6d8;
    --front-top: #d8474a;
    --front-bottom: #4a74b8;
    --paper: #ecebea;
    --paper-shade: #d9d8d6;
    --ink: #141414;
    --accent-red: #d8363a;
    --label-green: #3aa64a;
    --label-blue: #3f6fb8;
  }
  * { box-sizing: border-box; margin: 0; padding: 0; }
  html, body { width: 1200px; height: 800px; overflow: hidden; }
  body {
    background: var(--backdrop);
    display: flex;
    align-items: center;
    justify-content: center;
    gap: 70px;
  }
  .card {
    position: relative;
    width: 340px;
    height: 540px;
    overflow: hidden;
    box-shadow: 0 6px 18px rgba(0,0,0,0.22);
  }
  .brand-name {
    font-family: "Josefin Sans", sans-serif;
    font-weight: 700;
    color: var(--ink);
    text-transform: uppercase;
    line-height: 1.25;
  }
  .brand-name span { display: block; }

  /* Front */
  .card-front {
    background: linear-gradient(180deg, var(--front-top) 0%, #c98a9a 45%, var(--front-bottom) 100%);
  }
  .card-front .brand {
    position: absolute;
    left: 0; right: 0;
    top: 300px;
    display: flex;
    flex-direction: column;
    align-items: center;
  }
  .card-front .brand-name { font-size: 34px; letter-spacing: 1px; text-align: center; }
  .card-front .brand-name span { font-size: 15px; letter-spacing: 1.5px; }

  /* Back */
  .card-back {
    background: linear-gradient(160deg, var(--paper) 0%, #f6f5f4 45%, var(--paper-shade) 100%);
  }
  .card-back .facets { position: absolute; inset: 0; width: 100%; height: 100%; }
  .card-back .content {
    position: absolute;
    left: 48px; right: 24px;
    top: 70px;
  }
  .card-back .brand { display: flex; align-items: center; gap: 12px; }
  .brand-dot { width: 34px; height: 34px; border-radius: 50%; background: var(--accent-red); flex: none; }
  .card-back .brand-name { font-size: 24px; letter-spacing: 0.5px; }
  .card-back .brand-name span { font-size: 11px; letter-spacing: 1.2px; }
  .person { margin-top: 90px; font-family: "Questrial", sans-serif; }
  .person-name {
    font-family: "Josefin Sans", sans-serif;
    font-weight: 600;
    font-size: 24px;
    text-transform: uppercase;
    color: var(--ink);
  }
  .person-role { color: var(--accent-red); font-size: 15px; margin-top: 2px; }
  .contact { margin-top: 22px; }
  .contact-label { font-size: 12px; text-transform: uppercase; letter-spacing: 0.5px; }
  .contact-label.mobile { color: var(--label-green); }
  .contact-label.email { color: var(--label-blue); }
  .contact-value { font-size: 20px; color: var(--ink); margin-top: 2px; }
  .contact-value.small { font-size: 14px; }
</style>
</head>
<body>

  <section class="card card-front" aria-label="Card front">
    <div class="brand">
      <p class="brand-name">Corvallin<span>Property Solutions</span></p>
    </div>
  </section>

  <section class="card card-back" aria-label="Card back">
    <svg class="facets" viewBox="0 0 340 540" preserveAspectRatio="none" aria-hidden="true">
      <polygon points="0,120 340,40 340,60 0,150" fill="#ffffff" opacity="0.45"/>
      <polygon points="0,420 340,480 340,500 0,450" fill="#ffffff" opacity="0.35"/>
    </svg>
    <div class="content">
      <div class="brand">
        <div class="brand-dot"></div>
        <p class="brand-name">Corvallin<span>Property Solutions</span></p>
      </div>
      <div class="person">
        <p class="person-name">Tomas Brindle</p>
        <p class="person-role">Property Investor</p>
        <div class="contact">
          <p class="contact-label mobile">Mobile</p>
          <p class="contact-value">+44(0)7700845926</p>
        </div>
        <div class="contact">
          <p class="contact-label email">Email</p>
          <p class="contact-value small">tomas.corvallin@quilbrook.example</p>
        </div>
      </div>
    </div>
  </section>

</body>
</html>
```